Stationery Design Project

Hi All,

We need you to design stationary for a new Business and Accounting Advisory Firm. We have already got the logo designed and it is attached. If you could also if possible, match the fonts in your design to that on the logo’s provided.

What we need:
- Business Card
- A4 Letter head
- A4 Folders
- PPT template (Title page and regular page)

And what ever else you want to throw in.

We are in the process of getting the web site designed, however below is a list of websites which we like which will give you an understanding of the style that we are going for.

- plinvo.example
- brightmarrow.example
- tallyquill.example
- framelotus.example

I look forward to your seeing your design.
Updates

Hi All,

I have just realised that I forgot that i need to include a Bonded Ledgermen image on the letter head, please find attaced as File 1. Could you please have this image in the bottom left header.

Regards,

Morwen

Industry/Entity Type

Business

Requirements
Must have
• Outputs:
- Documents ready to print
- Generic editable information
- Pdf copies of the documents
- Word version of letterhead

```html
<!DOCTYPE html>
<html lang="en">
<head>
<meta charset="utf-8">
<title>Corvane Partners – Business Card</title>
<link href="https://fonts.googleapis.com/css2?family=Open+Sans:wght@400;600;700&display=swap" rel="stylesheet">
<style>
  :root {
    --bg: #ecebe8;
    --navy: #2f55a0;
    --blue: #3a74bb;
    --cyan: #45bcd9;
    --orange: #f7a21b;
    --ink: #262626;
    --rule: #c9c9c9;
    --white: #ffffff;
  }
  * { margin: 0; padding: 0; box-sizing: border-box; }
  html, body {
    width: 1200px; height: 900px; overflow: hidden;
    background: var(--bg);
    font-family: "Open Sans", Arial, sans-serif;
  }
  .canvas { position: relative; width: 1200px; height: 900px; }

  .card {
    position: absolute; width: 620px; height: 354px;
    box-shadow: 0 10px 24px rgba(0,0,0,.22);
    overflow: hidden;
  }

  /* Back of card */
  .card-back {
    left: 170px; top: 50px;
    background: linear-gradient(115deg, var(--navy) 0%, var(--blue) 45%, var(--cyan) 100%);
  }
  .card-back .brand-name {
    position: absolute; left: 0; right: 0; top: 138px;
    text-align: center;
    color: var(--white); font-weight: 700; font-size: 34px; letter-spacing: .3px;
  }

  /* Front of card */
  .card-front { left: 410px; top: 470px; background: var(--white); }
  .front-brand {
    position: absolute; left: 0; top: 96px; width: 290px;
    text-align: center;
    color: var(--navy); font-weight: 700; font-size: 25px; letter-spacing: .2px;
  }
  .divider {
    position: absolute; left: 290px; top: 34px; width: 1px; height: 230px;
    background: linear-gradient(to bottom, rgba(0,0,0,0), var(--rule) 30%, var(--rule) 70%, rgba(0,0,0,0));
  }
  .holder { position: absolute; left: 318px; top: 38px; }
  .holder-name { color: var(--navy); font-weight: 700; font-size: 17px; line-height: 22px; }
  .holder-role { color: var(--ink); font-size: 13px; line-height: 18px; }

  .contact-list { position: absolute; left: 318px; top: 110px; list-style: none; }
  .contact-list li {
    display: flex; align-items: flex-start; gap: 10px;
    color: var(--ink); font-size: 14px; line-height: 19px; margin-bottom: 5px;
  }
  .contact-icon { flex: none; width: 18px; height: 18px; margin-top: 1px; }

  .base-band {
    position: absolute; left: 0; bottom: 0; width: 100%; height: 34px;
    background: linear-gradient(90deg, var(--navy), var(--blue) 50%, var(--cyan));
    border-top: 3px solid var(--orange);
  }
</style>
</head>
<body>
<main class="canvas">

  <section class="card card-back" aria-label="Business card, back">
    <span class="brand-name">Corvane Partners</span>
  </section>

  <section class="card card-front" aria-label="Business card, front">
    <p class="front-brand">Corvane Partners</p>
    <div class="divider"></div>

    <div class="holder">
      <p class="holder-name">Dorian Vell</p>
      <p class="holder-role">Director</p>
    </div>

    <ul class="contact-list">
      <li>
        <svg class="contact-icon" viewBox="0 0 18 18" aria-hidden="true"><circle cx="9" cy="9" r="9" fill="var(--blue)"/><path d="M9 4a3 3 0 0 0-3 3c0 2.3 3 6 3 6s3-3.7 3-6a3 3 0 0 0-3-3zm0 4.2A1.2 1.2 0 1 1 9 5.8a1.2 1.2 0 0 1 0 2.4z" fill="#fff"/></svg>
        <span>Kestrelhof 8-B4<br>9999 ZZ, Marrowdam</span>
      </li>
      <li>
        <svg class="contact-icon" viewBox="0 0 18 18" aria-hidden="true"><circle cx="9" cy="9" r="9" fill="var(--blue)"/><path d="M6.2 4.5l1.6 2.2-.9 1c.6 1.2 1.5 2.1 2.7 2.7l1-.9 2.2 1.6-.8 1.6c-3.6-.3-6.8-3.5-7.1-7.1z" fill="#fff"/></svg>
        <span>555-014-2930</span>
      </li>
      <li>
        <svg class="contact-icon" viewBox="0 0 18 18" aria-hidden="true"><circle cx="9" cy="9" r="9" fill="var(--blue)"/><rect x="6" y="4.5" width="6" height="3" fill="#fff"/><rect x="4.5" y="7.5" width="9" height="4" rx="1" fill="#fff"/><rect x="6" y="10.5" width="6" height="3" fill="#fff" stroke="var(--blue)" stroke-width=".6"/></svg>
        <span>555-014-2939</span>
      </li>
      <li>
        <svg class="contact-icon" viewBox="0 0 18 18" aria-hidden="true"><circle cx="9" cy="9" r="9" fill="var(--blue)"/><text x="9" y="12.5" text-anchor="middle" font-size="10" font-weight="700" fill="#fff" font-family="Open Sans, sans-serif">@</text></svg>
        <span>dorian@corvanepartners.example</span>
      </li>
      <li>
        <svg class="contact-icon" viewBox="0 0 18 18" aria-hidden="true"><circle cx="9" cy="9" r="9" fill="var(--blue)"/><g fill="none" stroke="#fff" stroke-width="1"><circle cx="9" cy="9" r="4.5"/><ellipse cx="9" cy="9" rx="2" ry="4.5"/><path d="M4.5 9h9"/></g></svg>
        <span>www.corvanepartners.example</span>
      </li>
    </ul>

    <div class="base-band"></div>
  </section>

</main>
</body>
</html>
```